Savour and Thrive Wellbeing is being Launched and needs a business card and stationery package

I need a stationery package including business card (primary focus) , letterhead, digital letterhead, envelopes, with compliments slip, A 5 note sheet for the rebranding of my business and launch of my new website. I have a logo, like beige, brown earthy tones with a hint of red. I would also like the option of my letterhead also being printed on recycled paper in another format as well as the traditional letterhead. I do also send my letters to GPs and specialists digitally as well. I like to stand out from the usual stereotype of fruits and vegetables on business cards as I find that quite tacky and stereotypical. I want the business card to capture the essence of my logo as natural, nutrition, enjoyment, nurturing and freedom with food. I have attached the logo, and additional brief sheet on my ideas. Happy to have any background that is complementary to my theme, and what you believe would be catching. Definitely DONT'T like pink, try to pick up the darker colour in the logo please. and think too much black is a little overpowering.

Target Market(s)

clients who are interested in improving their health and wellness. Client 80% females; 20% males

Industry/Entity Type

Health And Wellness

Contact Information for Business Card

I am open to having different backgrounds as well that would complement the logo. Probably less emphasis on the heart out of the logo - just happy to keep that in the logo only please
I am also wanting two business cards - one for the appointments, one for general distribution and media distribution (both need to look consistent though) - but does give opportunity for one of the business cards to be less wordy and more striking. And the front of the business card can certainly stand out with the entire savour and thrive logo and my name and grab the attention of the receiver.
1st business card
on front:
Lorena Whitcombe
Savour and Thrive Wellbeing & logo
Nutritionist and Dietitian
Tarvel Medical Centre
647 Brindle Hill Rd, Quorrel Q 4987
Phone: (07) 3017 2968 Fax: (07) 3156 7209
Mobile: 0400 261 937
www.savourandthrivewellbeing.example.au
lorena@savourandthrivewellbeing.example.au
on back:
next appointment

……………………….. at ……………………… (possibly 4 times)
If you are unable to keep your appointment, please contact us as soon as possible (small font)
2nd business card (needs to be very eye catching and stand out)
on front: Savour and Thrive Wellbeing logo and my name
on back:
Lorena Whitcombe
address
phones, fax, website, email address

Font styles to use
Other font styles liked:
• please refer to logo

Requirements
Must have
• refreshing and simple; new and vibrant - I am rebranding my business after 20 years
• to get a feel of what is the theme - go to my new website (not completed as yet - but you will get a preliminary view) - don't do as google search as blocked - but can put into website header and it will be shown
• www.savourandthrivewellbeing.example.au - but please ignore the colouring of the 4 blocks under the slider on the home page - I am not wanting these colourings - they are getting updated.
Nice to have
• earthy tones, beige, hint of red, fonts to match logo if possible, organic, modern
• get inspiration from my logo please, open to having other backgrounds that complement
Should not have
• no food shots or stereotypical weight/ scales images
• no green, yellow or orange

```html
<!DOCTYPE html>
<html lang="en">
<head>
<meta charset="utf-8">
<title>Savour and Thrive Wellbeing – Business Card</title>
<link rel="stylesheet" href="https://fonts.googleapis.com/css2?family=Roboto+Condensed:wght@400&family=Arimo:wght@400&display=swap">
<style>
  :root {
    --backdrop: #333333;
    --paper-light: #ebe0a4;
    --paper-mid: #e3d591;
    --paper-dark: #d8c77c;
    --ink: #2c2a26;
    --ink-soft: #3d3a33;
    --brand: #3b2f2a;
    --accent-red: #e8321f;
    --white: #ffffff;
  }
  * { box-sizing: border-box; margin: 0; padding: 0; }
  html, body { width: 1200px; height: 1200px; overflow: hidden; }
  body {
    background: var(--backdrop);
    position: relative;
    font-family: "Roboto Condensed", "Arial Narrow", sans-serif;
    color: var(--ink);
  }
  .card {
    position: absolute;
    left: 238px;
    width: 726px;
    height: 416px;
    background: linear-gradient(135deg, var(--paper-light) 0%, var(--paper-mid) 55%, var(--paper-dark) 100%);
  }
  .card--front { top: 133px; }
  .card--back { top: 631px; font-family: "Arimo", Arial, sans-serif; }

  /* Front */
  .brand {
    position: absolute;
    left: 40px; top: 48px;
    width: 300px;
    text-align: center;
    color: var(--brand);
  }
  .brand__dot {
    display: block;
    width: 34px; height: 34px;
    margin: 0 auto 14px;
    border-radius: 50%;
    background: var(--brand);
  }
  .brand__name {
    font-size: 30px;
    line-height: 1.1;
    letter-spacing: 0.5px;
  }
  .name-ribbon {
    position: absolute;
    left: 467px; top: 84px;
    width: 259px; height: 33px;
    background: var(--accent-red);
    color: var(--white);
    font-size: 23px;
    line-height: 33px;
    padding-left: 16px;
    letter-spacing: 0.3px;
  }
  .job-title {
    position: absolute;
    left: 483px; top: 120px;
    font-size: 16px;
    color: var(--ink-soft);
  }
  .contact {
    position: absolute;
    font-size: 18px;
    line-height: 23px;
    color: var(--ink);
  }
  .contact--address { left: 34px; top: 222px; }
  .contact--phones { left: 34px; top: 267px; }
  .contact--online { right: 20px; top: 290px; text-align: right; font-size: 17px; }
  .contact__row { display: flex; align-items: center; gap: 6px; }
  .contact--online .contact__row { justify-content: flex-end; }
  .contact__indent { padding-left: 18px; }
  .icon { width: 12px; height: 12px; fill: var(--ink); flex: none; }

  /* Back */
  .appt-heading {
    position: absolute;
    top: 36px; left: 0; width: 100%;
    text-align: center;
    font-size: 18px;
  }
  .appt-line {
    position: absolute;
    left: 62px;
    width: 602px;
    display: flex;
    align-items: baseline;
    gap: 6px;
    font-size: 17px;
  }
  .appt-line__fill {
    flex: 1;
    border-bottom: 2px dotted var(--ink-soft);
    height: 14px;
  }
  .appt-line__at { width: 18px; text-align: center; }
  .appt-note {
    position: absolute;
    top: 366px; left: 0; width: 100%;
    text-align: center;
    font-size: 14px;
    color: var(--ink-soft);
  }
</style>
</head>
<body>

<section class="card card--front" aria-label="Business card front">
  <div class="brand">
    <span class="brand__dot"></span>
    <p class="brand__name">Savour and Thrive Wellbeing</p>
  </div>

  <div class="name-ribbon">LORENA WHITCOMBE</div>
  <p class="job-title">NUTRITIONIST AND DIETITIAN</p>

  <div class="contact contact--address">
    <p class="contact__row">
      <svg class="icon" viewBox="0 0 12 12"><path d="M6 0a4 4 0 0 0-4 4c0 3 4 8 4 8s4-5 4-8a4 4 0 0 0-4-4zm0 5.6A1.6 1.6 0 1 1 6 2.4a1.6 1.6 0 0 1 0 3.2z"/></svg>
      Tarvel Medical Centre
    </p>
    <p class="contact__indent">647 Brindle Hill Rd, Quorrel Q 4987</p>
  </div>

  <div class="contact contact--phones">
    <p class="contact__row">
      <svg class="icon" viewBox="0 0 12 12"><path d="M1 3c0-1 1-2 5-2s5 1 5 2v1H8V3H4v1H1zM2 5h8l1 6H1z"/></svg>
      (07) 3017 2968
    </p>
    <p class="contact__row">
      <svg class="icon" viewBox="0 0 12 12"><path d="M3 1h5v3H3zM1 5h10v6H1zm2 2v1h2V7zm4 0v1h2V7z"/></svg>
      (07) 3156 7209
    </p>
    <p class="contact__row">
      <svg class="icon" viewBox="0 0 12 12"><path d="M3.5 0h5a1 1 0 0 1 1 1v10a1 1 0 0 1-1 1h-5a1 1 0 0 1-1-1V1a1 1 0 0 1 1-1zm.5 2v7h4V2z"/></svg>
      0400 261 937
    </p>
  </div>

  <div class="contact contact--online">
    <p class="contact__row">
      www.savourandthrivewellbeing.example.au
      <svg class="icon" viewBox="0 0 12 12"><circle cx="6" cy="6" r="5.5"/></svg>
    </p>
    <p class="contact__row">
      lorena@savourandthrivewellbeing.example.au
      <svg class="icon" viewBox="0 0 12 12"><path d="M0 2.5h12v7H0zm1 1 5 3.2 5-3.2" stroke="#e3d591" stroke-width="0.8"/></svg>
    </p>
  </div>
</section>

<section class="card card--back" aria-label="Business card back">
  <p class="appt-heading">Next Appointment</p>

  <div class="appt-line" style="top:112px"><span class="appt-line__fill"></span><span class="appt-line__at">at</span><span class="appt-line__fill"></span></div>
  <div class="appt-line" style="top:175px"><span class="appt-line__fill"></span><span class="appt-line__at">at</span><span class="appt-line__fill"></span></div>
  <div class="appt-line" style="top:240px"><span class="appt-line__fill"></span><span class="appt-line__at">at</span><span class="appt-line__fill"></span></div>
  <div class="appt-line" style="top:304px"><span class="appt-line__fill"></span><span class="appt-line__at">at</span><span class="appt-line__fill"></span></div>

  <p class="appt-note">If you are unable to keep your appointment, please contact us as soon as possible</p>
</section>

</body>
</html>
```